Business Card & Logo

Business Card Design Project & Logo

Need logo for business card

Company name is ZORVA electric bikes USA

Target Market(s)

Consumer

Industry/Entity Type

Sporting Good

Contact Information for Business Card

Electric Bike Business Cards, Flyers, and LOGO.

Font styles to use
Sans Serif

Colors
ffc214
ffcf3e
faa54b
fee18a
f37122

Requirements
Must have
• New look &LOGO

```html
<!DOCTYPE html>
<html lang="en">
<head>
<meta charset="utf-8">
<title>ZORVA Electric Bikes USA – Business Card</title>
<link rel="stylesheet" href="https://fonts.googleapis.com/css2?family=Open+Sans:wght@400;600;700&display=swap">
<style>
  :root {
    --backdrop: #808080;
    --brand-orange: #f37122;
    --card-white: #ffffff;
    --card-black: #141414;
    --ink: #1c1c1c;
  }
  * { margin: 0; padding: 0; box-sizing: border-box; }
  html, body { width: 1200px; height: 900px; overflow: hidden; }
  body {
    background: var(--backdrop);
    font-family: "Open Sans", Arial, sans-serif;
    position: relative;
  }
  .card {
    position: absolute;
    top: 306px;
    width: 440px;
    height: 271px;
    border-radius: 12px;
    overflow: hidden;
  }
  .card-front { left: 149px; background: var(--card-white); }
  .card-back { left: 608px; background: var(--card-black); }

  .front-band {
    position: absolute; left: 0; top: 0;
    width: 100%; height: 87px;
    background: var(--brand-orange);
  }
  .front-wordmark {
    position: absolute; left: 23px; top: 16px;
    color: var(--card-white);
    font-weight: 600;
    line-height: 1;
  }
  .front-wordmark .wordmark-name { display: block; font-size: 44px; letter-spacing: 1px; }
  .front-wordmark .wordmark-tag { display: block; font-size: 14px; letter-spacing: 3.4px; margin-top: 5px; }

  .front-emblem {
    position: absolute; left: 277px; top: 8px;
    width: 104px; height: 104px;
    border-radius: 50%;
    background: var(--brand-orange);
    border: 5px solid var(--card-white);
  }

  .contact-block {
    position: absolute; left: 23px; top: 117px;
    color: var(--ink);
  }
  .contact-name {
    color: var(--brand-orange);
    font-weight: 700;
    font-size: 15px;
    line-height: 18px;
  }
  .contact-role { font-size: 12px; line-height: 14px; }
  .contact-list { list-style: none; margin-top: 13px; }
  .contact-list li {
    display: flex; align-items: center;
    font-size: 12.5px; line-height: 16px;
  }
  .contact-list svg { width: 9px; height: 9px; margin-right: 6px; fill: var(--brand-orange); }
  .contact-address { font-size: 12.5px; line-height: 16px; margin-top: 8px; }

  .back-emblem {
    position: absolute; left: 73px; top: 79px;
    width: 112px; height: 112px;
    border-radius: 50%;
    background: var(--brand-orange);
  }
  .back-wordmark {
    position: absolute; left: 204px; top: 104px;
    color: var(--brand-orange);
    font-weight: 600;
    line-height: 1;
  }
  .back-wordmark .wordmark-name { display: block; font-size: 42px; letter-spacing: 1px; }
  .back-wordmark .wordmark-tag { display: block; font-size: 14px; letter-spacing: 3px; margin-top: 4px; }
  .back-wordmark .wordmark-region { display: block; font-size: 9px; letter-spacing: 2px; margin-top: 3px; padding-left: 70px; }
</style>
</head>
<body>
  <section class="card card-front" aria-label="Business card front">
    <div class="front-band"></div>
    <div class="front-wordmark">
      <span class="wordmark-name">ZORVA</span>
      <span class="wordmark-tag">ELECTRIC BIKES</span>
    </div>
    <div class="front-emblem"></div>

    <div class="contact-block">
      <p class="contact-name">MAREN HOLLOWAY</p>
      <p class="contact-role">Managing Director</p>
      <ul class="contact-list">
        <li>
          <svg viewBox="0 0 10 10" aria-hidden="true"><path d="M2 0.5 L3.6 2.6 L2.7 3.8 Q3.8 6 6.2 7.3 L7.4 6.4 L9.5 8 L8.3 9.5 Q4.5 9.3 2.2 6.5 Q0.5 4.2 0.6 1.6 Z"/></svg>
          (044)987654321
        </li>
        <li>
          <svg viewBox="0 0 10 10" aria-hidden="true"><path d="M0.5 2 H9.5 V8 H0.5 Z M0.5 2 L5 5.3 L9.5 2" stroke="#fff" stroke-width="0.8"/></svg>
          hello@zorvamail.com
        </li>
        <li>
          <svg viewBox="0 0 10 10" aria-hidden="true"><circle cx="5" cy="5" r="4.6"/><path d="M5 0.5 V9.5 M0.5 5 H9.5 M5 0.5 Q2 5 5 9.5 M5 0.5 Q8 5 5 9.5" stroke="#fff" stroke-width="0.7" fill="none"/></svg>
          www.zorvarides.com
        </li>
      </ul>
      <p class="contact-address">5678, Harbor Lane,<br>Westfield, 24680</p>
    </div>
  </section>

  <section class="card card-back" aria-label="Business card back">
    <div class="back-emblem"></div>
    <div class="back-wordmark">
      <span class="wordmark-name">ZORVA</span>
      <span class="wordmark-tag">ELECTRIC BIKES</span>
      <span class="wordmark-region">USA</span>
    </div>
  </section>
</body>
</html>
```